Young and modern Electrical company working in the commercial arena.

Wanting a business card design thats modern and will last. Maybe Minimalist? Happy to look at changing my logo

Target Market(s)

Builders, Project Managers

Industry/Entity Type

Electrical

Contact Information for Business Card

Name
Address
Phone number
Job title

Logo Text

our name or just the logo i'm open to ideas

Font styles to use
Sans Serif

Requirements
Nice to have
• would like to keep the purple in our current logo. it's kinda unique to our market
Should not have
• Don't want it to be to busy. simple is best i think

```html
<!DOCTYPE html>
<html lang="en">
<head>
<meta charset="utf-8">
<title>Voltline Electrical – Business Card</title>
<link href="https://fonts.googleapis.com/css2?family=Lato:wght@400;700&family=Oswald:wght@500;600&display=swap" rel="stylesheet">
<style>
  :root {
    --purple: #5b3f9e;
    --purple-soft: #7a63b8;
    --ink: #1d1d1f;
    --ink-soft: #3a3a3c;
    --paper: #ffffff;
    --paper-shade: #eeeeef;
    --night: #1f1b1e;
    --night-edge: #2a2529;
    --silver: #cfcfd3;
    --stage: #e4e4e7;
  }
  * { margin: 0; padding: 0; box-sizing: border-box; }
  html, body { width: 1200px; height: 900px; overflow: hidden; }
  body {
    background: var(--stage);
    font-family: "Lato", Arial, sans-serif;
    display: flex;
    flex-direction: column;
    align-items: center;
    justify-content: center;
    gap: 40px;
  }
  .card {
    width: 640px;
    height: 366px;
    position: relative;
    box-shadow: 0 10px 30px rgba(0,0,0,.18);
  }
  /* Front */
  .card-front {
    background: radial-gradient(circle at 70% 35%, var(--paper) 0%, var(--paper-shade) 100%);
    color: var(--ink);
  }
  .identity {
    position: absolute;
    left: 44px;
    top: 48px;
    text-align: right;
  }
  .identity .person-name {
    font-family: "Oswald", "Arial Narrow", sans-serif;
    font-weight: 600;
    font-size: 40px;
    letter-spacing: 1px;
    color: var(--purple);
    text-transform: uppercase;
    line-height: 1;
  }
  .identity .job-title {
    font-size: 17px;
    color: var(--ink-soft);
    margin-top: 4px;
  }
  .accent-rule {
    position: absolute;
    left: 300px;
    top: 140px;
    width: 2px;
    height: 110px;
    background: var(--purple-soft);
    transform: rotate(28deg);
    transform-origin: top center;
  }
  .contact-list {
    position: absolute;
    left: 322px;
    top: 150px;
    list-style: none;
    font-size: 18px;
    line-height: 1.45;
  }
  .contact-list li { display: flex; align-items: center; gap: 10px; }
  .contact-list svg { width: 14px; height: 14px; fill: var(--purple); flex: none; }
  .contact-list .web-name { color: var(--purple); }
  .address {
    position: absolute;
    left: 44px;
    bottom: 40px;
    font-size: 17px;
    color: var(--ink-soft);
  }
  /* Back */
  .card-back {
    background: linear-gradient(160deg, var(--night-edge), var(--night));
  }
  .brand {
    position: absolute;
    left: 60px;
    top: 120px;
    display: flex;
    align-items: center;
    gap: 16px;
  }
  .brand-dot {
    width: 22px; height: 22px; border-radius: 50%;
    background: var(--purple);
  }
  .brand-name {
    font-family: "Lato", Arial, sans-serif;
    font-weight: 700;
    font-size: 52px;
    color: var(--silver);
    letter-spacing: 1px;
  }
  .brand-web {
    position: absolute;
    left: 98px;
    top: 210px;
    font-size: 18px;
    color: var(--silver);
  }
</style>
</head>
<body>
  <section class="card card-front">
    <div class="identity">
      <h1 class="person-name">Daniel Hart</h1>
      <p class="job-title">Director</p>
    </div>
    <div class="accent-rule"></div>
    <ul class="contact-list">
      <li><svg viewBox="0 0 24 24"><path d="M6.6 10.8a15 15 0 0 0 6.6 6.6l2.2-2.2c.3-.3.7-.4 1-.2 1.1.4 2.3.6 3.6.6.6 0 1 .4 1 1V20c0 .6-.4 1-1 1A17 17 0 0 1 3 4c0-.6.4-1 1-1h3.5c.6 0 1 .4 1 1 0 1.3.2 2.5.6 3.6.1.3 0 .7-.2 1z"/></svg>0400 123 456</li>
      <li><svg viewBox="0 0 24 24"><path d="M7 2h10a2 2 0 0 1 2 2v16a2 2 0 0 1-2 2H7a2 2 0 0 1-2-2V4a2 2 0 0 1 2-2zm0 3v12h10V5zm5 13.5a1 1 0 1 0 0 2 1 1 0 0 0 0-2z"/></svg>0411 987 654</li>
      <li><svg viewBox="0 0 24 24"><path d="M3 5h18a1 1 0 0 1 1 1v12a1 1 0 0 1-1 1H3a1 1 0 0 1-1-1V6a1 1 0 0 1 1-1zm1 2.2V17h16V7.2l-8 5.3z M5 7l7 4.6L19 7z"/></svg>admin@voltlineelectrical.com.au</li>
      <li><svg viewBox="0 0 24 24"><path d="M12 2a10 10 0 1 0 0 20 10 10 0 0 0 0-20zm6.9 9h-3a15 15 0 0 0-1.2-5.6A8 8 0 0 1 18.9 11zM12 4.1c.9 1.2 1.8 3.6 1.9 6.9h-3.8c.1-3.3 1-5.7 1.9-6.9zM9.3 5.4A15 15 0 0 0 8.1 11h-3a8 8 0 0 1 4.2-5.6zM5.1 13h3a15 15 0 0 0 1.2 5.6A8 8 0 0 1 5.1 13zm6.9 6.9c-.9-1.2-1.8-3.6-1.9-6.9h3.8c-.1 3.3-1 5.7-1.9 6.9zm2.7-1.3a15 15 0 0 0 1.2-5.6h3a8 8 0 0 1-4.2 5.6z"/></svg>www.<span class="web-name">voltlineelectrical</span>.com.au</li>
    </ul>
    <p class="address">Harbour Street, Newtown NSW, Australia</p>
  </section>

  <section class="card card-back">
    <div class="brand">
      <span class="brand-dot"></span>
      <span class="brand-name">voltline electrical</span>
    </div>
    <p class="brand-web">www.voltlineelectrical.com.au</p>
  </section>
</body>
</html>
```